Medical Office Needs an Updated Treatment Brochure

We need an updated brochure for a new treatment our offices are offering. The old brochure attached has all the current information on it, it just needs a new design.
We would like the updated version to be more modern and sleek as well as engaging.
Please see the old brochure attached for reference as well as this link: http://www.lumarvessa.com/medspa/iv-therapy/#1
The content from the attached brochure will remain.
UPDATE**** PLEASE SEE THE ATTACHED EXAMPLE BROCHURE OF THE DESIGN WE ARE LOOKING FOR!!
Thank you!!
Medical

```html
<!DOCTYPE html>
<html lang="en">
<head>
<meta charset="utf-8">
<title>Lumarvessa – IV Nutrient Therapy Brochure</title>
<link href="https://fonts.googleapis.com/css2?family=Roboto:wght@300;400&family=Roboto+Condensed:wght@300;400&display=swap" rel="stylesheet">
<style>
  :root{
    --page:#dedbd6;
    --paper:#ffffff;
    --ink:#2a2a2a;
    --body:#3a3a3a;
    --red:#e3262b;
    --blue:#2b9bd6;
    --brown:#7b5430;
    --green:#8cc540;
    --logo:#6cbf5a;
    --grey:#8a8a8a;
    --rule:#9a9a9a;
  }
  *{box-sizing:border-box;margin:0;padding:0}
  html,body{width:1200px;height:800px;overflow:hidden}
  body{background:var(--page);font-family:"Roboto Condensed",Arial,sans-serif;color:var(--body);position:relative}
  .sheet{position:absolute;top:200px;width:564px;height:400px;background:var(--paper);overflow:hidden}
  .sheet--inside{left:30px}
  .sheet--outside{left:606px}
  .block{position:absolute}
  .heading{font-family:"Roboto",Arial,sans-serif;font-weight:300;color:var(--ink);font-size:20px;line-height:1.15}
  .subhead{font-family:"Roboto Condensed",Arial,sans-serif;font-weight:300;font-size:8.5px;line-height:1.2}
  .subhead--red{color:var(--red)}
  .subhead--blue{color:var(--blue)}
  .subhead--brown{color:var(--brown)}
  .copy{font-size:5.4px;line-height:1.32;color:var(--body)}
  .copy p+p{margin-top:5px}
  .photo{position:absolute}
  .photo--fruit{left:0;top:204px;width:188px;height:114px;background:linear-gradient(120deg,#5a1e12 0%,#b5222a 28%,#3f6e22 55%,#c9dca0 70%,#8a1c25 100%)}
  .photo--dna{left:377px;top:226px;width:187px;height:90px;background:linear-gradient(135deg,#6cc3ee 0%,#2f8fd0 45%,#0c3f7a 100%)}
  .photo--drip-city{left:0;top:114px;width:182px;height:194px;background:linear-gradient(90deg,#8c8074 0%,#c9ab86 45%,#ecdcc4 75%,#ffffff 100%)}
  .photo--cover{left:330px;top:0;width:112px;height:400px;background:linear-gradient(180deg,#dfe7e6 0%,#eef3f3 45%,#d5e0e3 100%)}
  .quote{position:absolute;display:flex;align-items:center;justify-content:center;text-align:center;font-family:"Roboto",Arial,sans-serif;font-weight:300;font-size:10px;line-height:1.3;color:#444}
  .quote svg{position:absolute;top:0;height:100%;width:10px}
  .quote .brace-l{left:0}
  .quote .brace-r{right:0;transform:scaleX(-1)}
  .offer-grid{position:absolute;left:202px;top:160px;width:162px;height:230px}
  .offer-grid .divider-v{position:absolute;left:81px;top:8px;bottom:0;border-left:1px dashed var(--rule)}
  .offer-grid .divider-h{position:absolute;left:0;right:0;border-top:1px dashed var(--rule)}
  .offer{position:absolute;width:81px;text-align:center;font-size:8px;font-weight:400;color:var(--ink)}
  .offer .icon{display:block;width:22px;height:22px;border-radius:50%;margin:0 auto 3px;border:1px solid #cfd6cf}
  .icon--glamour{background:#dfe4e7}
  .icon--immunity{background:#d9b866}
  .icon--weight{background:#444}
  .icon--hangover{background:#b99a5e}
  .icon--detox{background:#c8552a}
  .icon--glutathione{background:#9b8a74}
  .icon--hydration{background:#5cb8e8}
  .icon--energy{background:#2a3f99}
  .brand{position:absolute;left:440px;top:64px;width:115px;font-family:"Roboto",Arial,sans-serif;font-weight:300;font-size:17px;color:var(--logo);display:flex;align-items:center;justify-content:flex-end;gap:4px}
  .brand .dot{width:7px;height:7px;border-radius:50%;background:var(--logo)}
  .cover-title{position:absolute;left:440px;top:106px;width:115px;text-align:right;font-family:"Roboto",Arial,sans-serif;font-weight:300;font-size:21px;line-height:1.15;color:var(--grey)}
  .cover-tagline{position:absolute;left:440px;top:158px;width:115px;text-align:right;font-size:5.5px;color:var(--grey)}
  .contact{position:absolute;left:242px;top:274px;width:86px;font-size:5.2px;line-height:1.35;color:var(--ink);font-style:normal}
  .contact .label{color:var(--green)}
  .contact .group+.group{margin-top:5px}
</style>
</head>
<body>

<section class="sheet sheet--inside" aria-label="Brochure inside spread">
  <h2 class="block heading" style="left:15px;top:10px">Ingredients</h2>
  <h3 class="block subhead subhead--red" style="left:15px;top:38px">What's In It?</h3>
  <p class="block copy" style="left:15px;top:49px;width:160px">A number of nutrients play well-defined roles in the maintenance of a robust immune response, optimal energy, and overall health.</p>
  <h3 class="block subhead subhead--red" style="left:15px;top:71px">Some of the amazing vitamins we use:</h3>
  <div class="block copy" style="left:15px;top:82px;width:162px">
    <p>Magnesium: Many people are lacking in this essential mineral. Magnesium is an excellent therapy for patients with heart disease, respiratory problems, migraines, and more. It helps with arrhythmias and can arrest an acute asthma attack. IV magnesium is also very relaxing, something we could all use.</p>
    <p>Vitamin C: IV administration fights off foreign invaders in your body and acts as a potent anti-histamine. From infections to cancer, the evidence of its powerful influence is simply astonishing when administered IV and in doses far too high for oral intake.</p>
    <p>Glutathione: This is the major super-antioxidant and detoxifying agent of our body. It cannot be taken orally but is made in the body. Whey protein and other nutritionals can help build glutathione in the body. It is severely depleted by mercury and chemicals. Many people exist with glutathione deficiency.</p>
  </div>
  <div class="photo photo--fruit" role="img" aria-label="Photo of fresh fruits, hibiscus flowers and a green juice"></div>
  <blockquote class="quote" style="left:28px;top:326px;width:140px;height:60px">
    <svg class="brace-l" viewBox="0 0 10 60" aria-hidden="true"><path d="M9 1 C3 1 5 28 1 30 C5 32 3 59 9 59" fill="none" stroke="#666" stroke-width=".8"/></svg>
    <span>"Our therapeutic suite"</span>
    <svg class="brace-r" viewBox="0 0 10 60" aria-hidden="true"><path d="M9 1 C3 1 5 28 1 30 C5 32 3 59 9 59" fill="none" stroke="#666" stroke-width=".8"/></svg>
  </blockquote>

  <h2 class="block heading" style="left:202px;top:12px">Our<br>Therapeutics<br>Suite</h2>
  <p class="block copy" style="left:202px;top:87px;width:162px">When you receive treatment sit comfortably in a recliner started and your specific is infused. During this time than 50 minutes, you may use your LapTop and go to work simply relax. A complete treatment requires a series of IV infusions with IV nutrients, you sit while a sterile IV line is composition of nutrients, which usually lasts less option for Plug in your PDA, read, watch TV, nap, or treatment course often sions.</p>
  <h2 class="block heading" style="left:202px;top:143px">What we offer</h2>
  <div class="offer-grid">
    <span class="divider-v"></span>
    <span class="divider-h" style="top:62px"></span>
    <span class="divider-h" style="top:119px"></span>
    <span class="divider-h" style="top:176px"></span>
    <div class="offer" style="left:0;top:15px"><span class="icon icon--glamour" aria-hidden="true"></span>Glamour</div>
    <div class="offer" style="left:81px;top:15px"><span class="icon icon--immunity" aria-hidden="true"></span>Immunity</div>
    <div class="offer" style="left:0;top:71px"><span class="icon icon--weight" aria-hidden="true"></span>Weight loss</div>
    <div class="offer" style="left:81px;top:71px"><span class="icon icon--hangover" aria-hidden="true"></span>Hangover</div>
    <div class="offer" style="left:0;top:128px"><span class="icon icon--detox" aria-hidden="true"></span>Detox</div>
    <div class="offer" style="left:81px;top:128px"><span class="icon icon--glutathione" aria-hidden="true"></span>Glutathione</div>
    <div class="offer" style="left:0;top:184px"><span class="icon icon--hydration" aria-hidden="true"></span>Hydration</div>
    <div class="offer" style="left:81px;top:184px"><span class="icon icon--energy" aria-hidden="true"></span>Energy</div>
  </div>

  <h2 class="block heading" style="left:391px;top:12px">Why it's Beneficial</h2>
  <h3 class="block subhead subhead--blue" style="left:391px;top:42px">Directly to the Source</h3>
  <div class="block copy" style="left:391px;top:54px;width:160px">
    <p>When vitamins, minerals, and other nutrients are infused intravenously (IV) they go directly into your bloodstream to fuel your cells. That means they avoid the potential loss of potency and poor absorption in the gastrointestinal (GI) tract that is a characteristic of nutrients taken orally.</p>
    <p>This makes IV nutrient administration a powerful therapy for numerous health concerns. In addition, super doses can be administered via IV without gastrointestinal side effects, which can limit dosing. A perfect example of this is vitamin C, which can only be taken in fairly small amounts orally before causing stomach upset. In contrast, super doses of vitamin C, which can be very beneficial for the immune system, can be administered safely and without stomach side effects with an intravenous delivery route.</p>
  </div>
  <h3 class="block subhead subhead--blue" style="left:391px;top:167px">Use IV Therapy to optimize your health</h3>
  <p class="block copy" style="left:391px;top:179px;width:160px">Proactive: Even if you're healthy, IV administration of a wide range of vitamins and minerals is an extremely effective way to boost your nutritional status, accelerate your athletic performance and prevent illness. It is especially important when flu season is around, or before and during stressful situations.</p>
  <div class="photo photo--dna" role="img" aria-label="Blue illustration of DNA strands"></div>
  <blockquote class="quote" style="left:400px;top:326px;width:150px;height:60px">
    <svg class="brace-l" viewBox="0 0 10 60" aria-hidden="true"><path d="M9 1 C3 1 5 28 1 30 C5 32 3 59 9 59" fill="none" stroke="#666" stroke-width=".8"/></svg>
    <span>"...Super doses can be<br>administered via IV without<br>intestinal side effects..."</span>
    <svg class="brace-r" viewBox="0 0 10 60" aria-hidden="true"><path d="M9 1 C3 1 5 28 1 30 C5 32 3 59 9 59" fill="none" stroke="#666" stroke-width=".8"/></svg>
  </blockquote>
</section>

<section class="sheet sheet--outside" aria-label="Brochure outside spread">
  <h2 class="block heading" style="left:15px;top:12px">The Facts</h2>
  <h3 class="block subhead subhead--brown" style="left:15px;top:38px">What is IV Therapy?</h3>
  <div class="block copy" style="left:15px;top:53px;width:165px">
    <p>IV Nutrient Therapy involves the direct administration of vital minerals, nutrients and vitamins directly into the bloodstream (intravenously infused) through an IV drip.</p>
    <p>These essential nutrients can help boost immune function, increase energy levels, assist in weight management, avoid chronic health issues, and even aid in skin rejuvenation.</p>
  </div>
  <div class="photo photo--drip-city" role="img" aria-label="Photo of an IV drip bag in front of a sunlit city skyline"></div>
  <blockquote class="quote" style="left:28px;top:326px;width:142px;height:60px">
    <svg class="brace-l" viewBox="0 0 10 60" aria-hidden="true"><path d="M9 1 C3 1 5 28 1 30 C5 32 3 59 9 59" fill="none" stroke="#666" stroke-width=".8"/></svg>
    <span>"IV Therapy is great for<br>boosting health and<br>preventing illness."</span>
    <svg class="brace-r" viewBox="0 0 10 60" aria-hidden="true"><path d="M9 1 C3 1 5 28 1 30 C5 32 3 59 9 59" fill="none" stroke="#666" stroke-width=".8"/></svg>
  </blockquote>

  <address class="contact">
    <div class="group"><span class="label">Lumarvessa</span><br>2710 Orchard Lane<br>Fairvale CA 90210</div>
    <div class="group"><span class="label">Lumarvessa Southwest</span><br>8840 Linden Avenue, Suite<br>310 Fairvale, CA 90212</div>
    <div class="group"><span class="label">W:</span> www.lumarvessa.com<br><span class="label">E:</span> appointments@lumarvessa.com<br><span class="label">P:</span> 844-Lumarvessa</div>
  </address>

  <div class="photo photo--cover" role="img" aria-label="Cover photo of a clear IV drip chamber"></div>
  <div class="brand"><span class="dot" aria-hidden="true"></span>Lumarvessa</div>
  <h1 class="cover-title">IV&nbsp; Nutrient<br>Therapy</h1>
  <p class="cover-tagline">Revitalize | Recharge | Rejuvenate!</p>
</section>

</body>
</html>
```